Pediatric Vision Care: Myopia Control Brochure

We are a pediatric eye care practice (ophthalmology and optometry). One of our services we offer for children is myopia control, which are strategies for slowing or stopping the progression of nearsightedness. This is a service we need to sell to parents because most insurance won't pay for it. There are different options we offer that can work well for kids in different situations: glasses with Corvane lenses, atropine eye drops, and/or special contact lenses. We need a brochure we can distribute to parents to let them know about this service that would encourage them to buy it for children who need it. Attached is our initial draft brochure created by our staff that provides text that we want to keep. The images and layout can change. We probably need at least one or two photos of kids on the brochure, because this is only something that works for children who are still growing, and the target audience is parents of 4-8 year old children.

Target Market(s)

Parents of 4-8 year old children

Font styles to use
Sans Serif

Requirements
Must have
• I'm uploading our company logo that should be included somewhere on the brochure. You can include contact information (web address, phone number) for our practice that is found on our website: http://www.brookhollowkidsvision.com/
Should not have
• This should not look childish. We need the impression to be friendly but professional, medical, expert.

```html
<!DOCTYPE html>
<html lang="en">
<head>
<meta charset="utf-8">
<title>Myopia Control Brochure – Brookhollow Kids Vision</title>
<link href="https://fonts.googleapis.com/css2?family=Poppins:wght@300;400;600;700&family=Arimo:ital,wght@0,400;0,700;1,400&display=swap" rel="stylesheet">
<style>
:root{
  --ink:#231f20;
  --purple:#6b6fbf;
  --green:#8dc63f;
  --yellow:#f2c12e;
  --orange:#f7941d;
  --paper:#ffffff;
  --backdrop:#dcdcdc;
  --body:#333333;
  --rule:#bbbbbb;
}
*{box-sizing:border-box;margin:0;padding:0}
html,body{width:1200px;height:1022px;overflow:hidden;background:var(--backdrop)}
body{position:relative;font-family:"Arimo",Arial,sans-serif;color:var(--body)}
.spread{position:absolute;left:245px;width:930px;height:656px;background:var(--paper);transform:scale(0.763);transform-origin:0 0;box-shadow:0 2px 6px rgba(0,0,0,.12);overflow:hidden}
.spread--inside{top:6px}
.spread--outside{top:516px}
.abs{position:absolute}
.h-panel{font-family:"Poppins",sans-serif;font-weight:300;font-size:27px;line-height:1}
.h-panel b{font-weight:700}
.stripe{position:absolute;height:6px;width:148px;display:flex}
.stripe span{flex:1}
.stripe span:nth-child(1){background:var(--purple)}
.stripe span:nth-child(2){background:var(--green)}
.stripe span:nth-child(3){background:var(--yellow)}
.stripe span:nth-child(4){background:var(--orange)}
.copy{font-size:10.5px;line-height:13.2px;color:var(--body)}
.copy p+p{margin-top:13px}
.aside{font-size:10.5px;line-height:12px;font-style:italic}
.brand{position:absolute;display:flex;align-items:center;gap:6px;font-family:"Poppins",sans-serif;font-weight:600;color:var(--ink);white-space:nowrap}
.brand i{display:block;border-radius:50%;background:var(--green)}
.photo{position:absolute}
.eye-diagram{position:absolute;background:linear-gradient(135deg,#f4ddd0,#e9b9a3)}
.label{font-size:10.5px;color:var(--body)}
.t-purple{color:var(--purple)}
.t-green{color:var(--green)}
.t-orange{color:var(--orange)}
.contact-row{position:absolute;left:325px;width:280px;display:flex;gap:12px}
.contact-row .aside{width:72px;flex:none;color:var(--orange)}
.contact-row .copy{font-size:10px;line-height:12px}
.info-block{position:absolute;font-size:10px;line-height:12px;white-space:nowrap}
.info-block strong{display:block;color:var(--ink)}
.divider{position:absolute;width:1px;background:var(--rule)}
</style>
</head>
<body>

<section class="spread spread--inside">
  <h1 class="abs h-panel" style="left:25px;top:32px;font-size:26px;color:var(--ink)"><b>Myopia</b> control</h1>
  <div class="brand" style="left:786px;top:34px;font-size:10px"><i style="width:9px;height:9px"></i>Brookhollow Kids Vision</div>

  <article>
    <h2 class="abs h-panel t-purple" style="left:25px;top:90px">Lumira Corvane<br><b>glasses lenses</b></h2>
    <div class="stripe" style="left:25px;top:157px"><span></span><span></span><span></span><span></span></div>
    <div class="photo" role="img" aria-label="Corvane spectacle lens with concentric ring optics, labelled control myopia progression and correct myopia" style="left:25px;top:186px;width:263px;height:233px;background:linear-gradient(135deg,#5a9aa3,#2f6f7c 60%,#1e4f5c)"></div>
    <p class="abs aside t-purple" style="left:25px;top:440px;width:85px">We offer the largest selection of children's glasses frames</p>
    <div class="abs copy" style="left:117px;top:434px;width:178px">
      <p>FDA market authorized Lumira Corvane glasses lenses have been shown to slow myopia progression by about 50% in children aged 6-12.</p>
      <p>These lenses are a great treatment option because all your child needs to do is wear glasses. They look</p>
      <p>almost identical to ordinary glasses, but use specialized optics to signal the brain to slow the growth of myopic eyes.&nbsp;&nbsp; options</p>
    </div>
  </article>

  <article>
    <h2 class="abs h-panel t-green" style="left:413px;top:90px">Low-dose<br><b>atropine</b></h2>
    <div class="stripe" style="left:413px;top:157px"><span></span><span></span><span></span><span></span></div>
    <div class="abs copy" style="left:413px;top:187px;width:190px">
      <p>These eyedrops have been studied for over 20 years and have been shown to slow myopia progression by about 50% when used consistently.</p>
      <p>Low-dose atropine is simple to add to your daily routine.&nbsp; One drop is placed in each eye before bed each evening. These are ordered from a compounding pharmacy and mailed directly to your home.</p>
    </div>
    <p class="abs aside t-green" style="left:341px;top:261px;width:68px">Low dose atropine is often used for myopia control in children</p>
    <div class="photo" role="img" aria-label="Eyedrop bottle tip releasing a single drop" style="left:341px;top:353px;width:259px;height:264px;background:linear-gradient(160deg,#4b5a63,#1d272d 70%)"></div>
  </article>

  <article>
    <h2 class="abs h-panel t-orange" style="left:649px;top:90px">Specialty<br><b>contact lenses</b></h2>
    <div class="stripe" style="left:649px;top:157px"><span></span><span></span><span></span><span></span></div>
    <div class="photo" role="img" aria-label="Soft contact lens balanced on a fingertip" style="left:650px;top:185px;width:253px;height:255px;background:linear-gradient(120deg,#1a1a1a,#6b3a2c 55%,#c9826a)"></div>
    <p class="abs aside t-orange" style="left:650px;top:462px;width:82px">We discuss the various contact lenses available and determine the best option based on your individual needs and lifestyle</p>
    <div class="abs copy" style="left:745px;top:462px;width:160px">
      <p>FDA-approved ClearPath lenses have been shown to slow myopia progression by about 50% in children aged 8-12.</p>
      <p>Contact lenses can be a great fit for many children, especially active children or those who do not enjoy wearing glasses. Many children as young as 7 or 8 are successful at wearing contacts.</p>
    </div>
  </article>
</section>

<section class="spread spread--outside">
  <article>
    <h2 class="abs h-panel t-green" style="left:50px;top:25px;font-weight:700;font-size:27px">Environmental<br>options:</h2>
    <div class="stripe" style="left:50px;top:90px"><span></span><span></span><span></span><span></span></div>
    <div class="abs copy" style="left:50px;top:112px;width:240px">
      <p>All myopic children can benefit from these lifestyle changes.</p>
      <p>It is important to get your child outdoors consistently. There is strong evidence that children who spend at least 2 hours a day outdoors are less likely to become myopic, and their myopia progresses slower than children who are outdoors less. Some studies show that increasing outdoor time by as few as 45 minutes a day is beneficial in reducing progression.</p>
      <p>There is some evidence that consistent use of screens, particularly held very close to the face, can worsen nearsightedness. We recommend limiting non-academic screen time and near work, and encourage your child to use the 20-20-20 rule. Every 20 minutes take a 20 second break to look at least 20 feet away.</p>
    </div>
    <div class="photo" role="img" aria-label="Girl in sport glasses holding a soccer ball outside a brick building" style="left:0;top:380px;width:305px;height:276px;background:linear-gradient(170deg,#7c6a5c,#5e6b4a 55%,#3e4a34)"></div>
  </article>

  <article>
    <div class="photo" role="img" aria-label="Three children in sport glasses crouching with soccer balls in front of the practice sign" style="left:305px;top:0;width:308px;height:187px;background:linear-gradient(180deg,#8a5a4a,#6e7a5a 60%,#4c6138)"></div>
    <h2 class="abs h-panel" style="left:325px;top:200px;font-size:21px;color:var(--ink)"><b>Contact</b> and<br><b>scheduling</b> info</h2>
    <div class="stripe" style="left:325px;top:257px"><span></span><span></span><span></span><span></span></div>

    <div class="contact-row" style="top:283px">
      <p class="aside">1.&nbsp; If you are a new patient to our practice:</p>
      <div class="copy">Fill out the new patient intake form and email it to us at <strong>appointments@brookhollowkidsvision.com</strong></div>
    </div>
    <div class="contact-row" style="top:355px">
      <p class="aside">2.&nbsp; If you are an established patient, you can schedule an appointment by either:</p>
      <div class="copy">
        <p><strong>Calling</strong> us at <strong>(555) 210-0140</strong>, and selecting option 1 to speak with a scheduler. It is much more effective on a busy day to leave us a voicemail.</p>
        <p style="margin-top:8px"><strong class="t-orange">or:</strong> <strong>Emailing</strong> us at <strong>appointments@brookhollowkidsvision.com.</strong> Please include a phone number where we can reach you if needed.</p>
        <p style="margin-top:8px"><strong class="t-orange">or:</strong> <strong>Texting</strong> us at (555) 210-0177.</p>
      </div>
    </div>
    <div class="abs" style="left:325px;top:507px;width:275px;height:1px;background:var(--purple)"></div>
    <div class="info-block" style="left:330px;top:533px"><strong>Mailing Address</strong>Brookhollow Kids Vision<br>2180 Harbor Lane<br>Brookhollow, VA 23400</div>
    <div class="divider" style="left:492px;top:533px;height:55px"></div>
    <div class="info-block" style="left:502px;top:536px"><strong>Telephone</strong>Voice: (555) 210-0140<br>Text: (555) 210-0177<br>Fax: (555) 210-0199</div>
    <div class="info-block" style="left:330px;top:595px;font-size:9.5px"><strong style="font-size:10px">Email</strong>info@brookhollowkidsvision.com</div>
    <div class="divider" style="left:492px;top:595px;height:24px"></div>
    <div class="info-block" style="left:502px;top:595px;font-size:9.5px"><strong style="font-size:10px">Website</strong>brookhollowkidsvision.com</div>
  </article>

  <article>
    <div class="brand" style="left:690px;top:50px;font-size:15px"><i style="width:14px;height:14px"></i>Brookhollow Kids Vision</div>
    <h1 class="abs" style="left:655px;top:92px;font-family:'Poppins',sans-serif;color:var(--ink);font-size:63px;line-height:60px"><b style="font-weight:700">Myopia</b><br><span style="font-weight:300">control</span></h1>
    <div class="stripe" style="left:658px;top:230px"><span></span><span></span><span></span><span></span></div>
    <div class="eye-diagram" role="img" aria-label="Cross-section illustration comparing a myopic eye with a normal eye" style="left:722px;top:250px;width:190px;height:140px"></div>
    <p class="abs label" style="left:657px;top:293px">Myopic Eye</p>
    <p class="abs label" style="left:657px;top:344px">Normal Eye</p>
    <div class="abs copy" style="left:686px;top:408px;width:228px">
      <p>Myopia or nearsightedness causes blurry distance vision. Myopia is caused by the elongation of the eye, and progresses throughout childhood. Myopia is becoming increasingly common. More severe myopia and a higher glasses prescription is associated with a higher risk of eye problems involving the retina in adulthood, such as retinal problems and macular degeneration.</p>
      <p>Myopia control is meant to slow the growth of the eye, keeping the glasses prescription as low as possible and reducing the risk of ocular disease in adulthood.</p>
      <p>There are several treatment options</p>
    </div>
  </article>
</section>

</body>
</html>
```